Travel Ad restaurant table

add 6 w 4 t, it is a table top add
needs logo
wed site www.quillmorejourneys.com
phone 800.517.6294
find use code
tag line: So what’s the buzz all about? Discover how Quillmore Journeys can craft your next great escape:
vacation location pictures see sample. Europe, US, Asia
Target Market(s)
local Customers Travel
Industry/Entity Type
travel
Requirements
Must have
- 1 week
Nice to have
- table top in restaurant op out clear

```html
<!DOCTYPE html>
<html lang="en">
<head>
<meta charset="utf-8">
<title>Quillmore Journeys – Table Top Ad</title>
<link href="https://fonts.googleapis.com/css2?family=Alegreya:ital,wght@0,700;0,800;1,700&family=Poppins:wght@600;700&display=swap" rel="stylesheet">
<style>
  :root {
    --stage: #e6e6e6;
    --paper: #ffffff;
    --bee-yellow: #fde619;
    --pale-yellow: #fbf08a;
    --ink: #141414;
    --honey-brown: #8a5a12;
    --grid-line: #1a1a1a;
  }
  * { box-sizing: border-box; margin: 0; padding: 0; }
  html, body { width: 971px; height: 1200px; overflow: hidden; }
  body { background: var(--stage); position: relative; }

  .tent-card {
    position: absolute; left: 20px; top: 290px;
    width: 931px; height: 621px;
    background: var(--paper);
    overflow: hidden;
  }
  .accent { position: absolute; background: var(--bee-yellow); }
  .accent.soft { background: var(--pale-yellow); }
  .grid-patch { position: absolute; }

  .photo { position: absolute; }
  .photo--santorini-sunset { left: 19px; top: 26px; width: 257px; height: 189px;
    background: linear-gradient(160deg, #f3c48c 0%, #d88b5a 45%, #4d6f86 100%); }
  .photo--white-stairs { left: 19px; top: 238px; width: 259px; height: 335px;
    background: linear-gradient(180deg, #cfe0f0 0%, #f4f1ec 40%, #d9cdbd 75%, #8fb4d6 100%); }
  .photo--old-town-dusk { left: 291px; top: 30px; width: 363px; height: 102px;
    background: linear-gradient(180deg, #f4a532 0%, #c8743a 45%, #4a3a42 100%); }
  .photo--city-coast { left: 670px; top: 26px; width: 240px; height: 153px;
    background: linear-gradient(180deg, #a9cde6 0%, #6f9a8a 45%, #1ea2b5 100%); }
  .photo--night-beach { left: 670px; top: 224px; width: 240px; height: 176px;
    background: linear-gradient(170deg, #2d4f8c 0%, #3f7bb8 45%, #d9a86a 70%, #18a2cf 100%); }
  .photo--seaside-dinner { left: 670px; top: 421px; width: 240px; height: 176px;
    background: linear-gradient(180deg, #efe2c8 0%, #c9b49a 50%, #5e5048 100%); }

  .brand {
    position: absolute; left: 291px; top: 175px; width: 363px;
    display: flex; align-items: center; justify-content: center; gap: 12px;
  }
  .brand-dot { width: 34px; height: 34px; border-radius: 50%; background: var(--bee-yellow); }
  .brand-name {
    font-family: "Alegreya", Georgia, serif; font-weight: 700;
    font-size: 38px; line-height: 1; color: var(--ink);
  }

  .headline {
    position: absolute; left: 291px; top: 290px; width: 363px;
    text-align: center; font-family: "Alegreya", Georgia, serif;
    font-weight: 800; font-size: 33px; line-height: 1.15; color: var(--ink);
  }
  .subline {
    position: absolute; left: 291px; top: 380px; width: 363px;
    text-align: center; font-family: "Alegreya", Georgia, serif;
    font-weight: 700; font-style: italic; font-size: 20px; line-height: 1.3;
    color: var(--honey-brown);
  }

  .promo-code {
    position: absolute; left: 319px; top: 453px; width: 321px; height: 32px;
    background: var(--bee-yellow);
    font-family: "Poppins", Arial, sans-serif; font-weight: 700; font-size: 18px;
    color: var(--ink); display: flex; align-items: center; justify-content: center;
  }
  .contact-box {
    position: absolute; left: 305px; top: 485px; width: 349px; height: 113px;
    background: var(--ink); color: var(--bee-yellow);
    display: flex; flex-direction: column; align-items: center; justify-content: center;
    gap: 2px;
  }
  .contact-label { font-family: "Poppins", Arial, sans-serif; font-weight: 600; font-size: 17px; }
  .contact-phone {
    font-family: "Poppins", Arial, sans-serif; font-weight: 700; font-size: 32px; line-height: 1.1;
    display: flex; align-items: center; gap: 8px;
  }
  .contact-web { font-family: "Alegreya", Georgia, serif; font-weight: 700; font-size: 19px; }
</style>
</head>
<body>
  <main class="tent-card">
    <div class="accent" style="left:0;top:0;width:70px;height:24px"></div>
    <div class="accent" style="left:300px;top:0;width:170px;height:24px"></div>
    <div class="accent" style="left:620px;top:10px;width:90px;height:22px"></div>
    <div class="accent" style="left:880px;top:0;width:51px;height:60px"></div>
    <div class="accent" style="left:0;top:250px;width:18px;height:120px"></div>
    <div class="accent" style="left:900px;top:180px;width:31px;height:90px"></div>
    <div class="accent" style="left:0;top:560px;width:90px;height:61px"></div>
    <div class="accent" style="left:540px;top:600px;width:160px;height:21px"></div>
    <div class="accent" style="left:880px;top:560px;width:51px;height:61px"></div>
    <div class="accent soft" style="left:160px;top:22px;width:60px;height:12px"></div>
    <div class="accent soft" style="left:730px;top:210px;width:70px;height:14px"></div>
    <div class="accent soft" style="left:100px;top:232px;width:60px;height:12px"></div>

    <svg class="grid-patch" style="left:0;top:0" width="70" height="70" viewBox="0 0 70 70" aria-hidden="true">
      <g stroke="var(--grid-line)" stroke-width="1" fill="none">
        <path d="M0 14H70M0 28H70M0 42H70M0 56H70M14 0V70M28 0V70M42 0V70M56 0V70"/>
      </g>
    </svg>
    <svg class="grid-patch" style="left:150px;top:555px" width="110" height="66" viewBox="0 0 110 66" aria-hidden="true">
      <g stroke="var(--grid-line)" stroke-width="1" fill="none">
        <path d="M0 14H110M0 28H110M0 42H110M0 56H110M14 0V66M28 0V66M42 0V66M56 0V66M70 0V66M84 0V66M98 0V66"/>
      </g>
    </svg>
    <svg class="grid-patch" style="left:860px;top:380px" width="71" height="70" viewBox="0 0 71 70" aria-hidden="true">
      <g stroke="var(--grid-line)" stroke-width="1" fill="none">
        <path d="M0 14H71M0 28H71M0 42H71M0 56H71M14 0V70M28 0V70M42 0V70M56 0V70"/>
      </g>
    </svg>

    <div class="photo photo--santorini-sunset" role="img" aria-label="Greek island village with stone tower at sunset over the sea"></div>
    <div class="photo photo--white-stairs" role="img" aria-label="Whitewashed Santorini stairway with blue doors and pink flowers"></div>
    <div class="photo photo--old-town-dusk" role="img" aria-label="European hilltop old town skyline at dusk"></div>
    <div class="photo photo--city-coast" role="img" aria-label="Coastal city skyline with turquoise lagoon and park"></div>
    <div class="photo photo--night-beach" role="img" aria-label="Beachfront hotels along a curved bay at twilight"></div>
    <div class="photo photo--seaside-dinner" role="img" aria-label="Couple toasting at a seaside dinner table at sunset"></div>

    <div class="brand">
      <span class="brand-dot"></span>
      <span class="brand-name">Quillmore Journeys</span>
    </div>

    <h1 class="headline">So what’s the buzz<br>all about?</h1>
    <p class="subline">Discover how Quillmore Journeys<br>can craft your next great escape:</p>

    <div class="promo-code">Find use code: #GVT123987J</div>
    <div class="contact-box">
      <span class="contact-label">Contact Us</span>
      <span class="contact-phone">
        <svg width="28" height="28" viewBox="0 0 28 28" aria-hidden="true">
          <circle cx="14" cy="14" r="14" fill="var(--bee-yellow)"/>
          <path d="M10 7.5c.6-.4 1.3-.2 1.6.4l1.3 2.6c.3.6.1 1.2-.4 1.6l-1 .8c.8 1.7 2 2.9 3.6 3.7l.8-1c.4-.5 1.1-.7 1.6-.4l2.6 1.3c.6.3.8 1 .4 1.6l-.9 1.4c-.5.8-1.5 1.1-2.4.8-4.2-1.4-7-4.2-8.4-8.4-.3-.9 0-1.9.8-2.4z" fill="var(--ink)"/>
        </svg>
        800.517.6294
      </span>
      <span class="contact-web">www.quillmorejourneys.com</span>
    </div>
  </main>
</body>
</html>
```